Roaming outings business card

please see website
www.roamingoutings.comau

info needed on card
Keiran Voss
Ph
email
Adventure Riding GPS trails

please use my logo and colours off my site

Business

Keiran Voss
keiran@roamingoutings.com

```html
<!DOCTYPE html>
<html lang="en">
<head>
<meta charset="utf-8">
<title>Roaming outings business card</title>
<link rel="stylesheet" href="https://fonts.googleapis.com/css2?family=Quicksand:wght@300;700&family=Tinos&display=swap">
<style>
  :root {
    --backdrop: #e4e3e3;
    --card: #f7f7f7;
    --ink: #1a1a1a;
    --yellow: #ffcc00;
    --grey-light: #d4d4d4;
    --grey-dark: #6b6b6b;
  }
  * { margin: 0; padding: 0; box-sizing: border-box; }
  html, body { width: 1200px; height: 1000px; overflow: hidden; }
  body { background: var(--backdrop); position: relative; }
  .card {
    position: absolute;
    top: 200px;
    width: 340px;
    height: 600px;
    background: var(--card);
    overflow: hidden;
    box-shadow: 0 10px 30px rgba(0,0,0,0.18);
  }
  .card--front { left: 220px; }
  .card--back { left: 640px; }
  .bands { position: absolute; left: 0; top: 0; width: 340px; height: 600px; }
  .brand {
    position: absolute;
    left: 0; right: 0;
    display: flex;
    align-items: center;
    justify-content: center;
    gap: 10px;
    font-family: "Quicksand", sans-serif;
    font-weight: 700;
    font-size: 26px;
    color: var(--ink);
  }
  .brand__dot {
    width: 28px; height: 28px;
    border-radius: 50%;
    background: var(--yellow);
  }
  .card--front .brand { top: 225px; }
  .card--back .brand { top: 150px; }
  .holder {
    position: absolute;
    top: 222px; left: 0; right: 0;
    text-align: center;
    font-family: "Quicksand", sans-serif;
    font-weight: 300;
    font-size: 34px;
    color: var(--ink);
    letter-spacing: 1px;
  }
  .contact {
    position: absolute;
    top: 300px; left: 0; right: 0;
    font-family: "Tinos", serif;
    font-size: 15px;
    color: var(--ink);
    text-align: center;
    line-height: 26px;
  }
  .contact__line { display: flex; align-items: center; justify-content: center; gap: 6px; }
  .contact__icon { width: 15px; height: 13px; }
</style>
</head>
<body>
  <section class="card card--front" aria-label="Card front">
    <svg class="bands" viewBox="0 0 340 600" aria-hidden="true">
      <polygon points="0,470 340,440 340,462 0,492" fill="var(--yellow)"/>
      <polygon points="0,492 340,462 340,510 0,530" fill="var(--grey-light)"/>
      <polygon points="0,530 340,510 340,600 0,600" fill="var(--grey-dark)"/>
    </svg>
    <div class="brand"><span class="brand__dot"></span>Roaming outings</div>
  </section>

  <section class="card card--back" aria-label="Card back">
    <svg class="bands" viewBox="0 0 340 600" aria-hidden="true">
      <polygon points="0,470 340,440 340,470 0,495" fill="var(--grey-dark)"/>
      <polygon points="0,495 340,470 340,510 0,528" fill="var(--grey-light)"/>
      <polygon points="0,528 340,510 340,600 0,600" fill="var(--yellow)"/>
    </svg>
    <div class="brand"><span class="brand__dot"></span>Roaming outings</div>
    <p class="holder">Keiran Voss</p>
    <div class="contact">
      <p class="contact__line">
        <svg class="contact__icon" viewBox="0 0 15 13" aria-hidden="true">
          <path d="M1 4 Q7.5 -1 14 4 L12 6 L10 4.5 L10 3.5 Q7.5 2.5 5 3.5 L5 4.5 L3 6 Z" fill="var(--ink)"/>
          <rect x="3" y="6" width="9" height="6" rx="1" fill="var(--ink)"/>
        </svg>
        0198-765-432
      </p>
      <p class="contact__line">
        <svg class="contact__icon" viewBox="0 0 15 11" aria-hidden="true">
          <rect x="0.5" y="0.5" width="14" height="10" fill="none" stroke="var(--ink)"/>
          <path d="M0.5 0.5 L7.5 6 L14.5 0.5" fill="none" stroke="var(--ink)"/>
        </svg>
        keiran@roamingoutings.com
      </p>
    </div>
  </section>
</body>
</html>
```